Lanternfield Drinks business cards

We need a business card design for our new logo. The company is modern, progressive, professional, yet approachable. The key products are ready to drink bottles and cans of coffee based beverages.
These cards will be a critical part of the first impression made by our sales organization, business development team, and all external facing personnel.
Card can be a vertical or horizontal orientation.

Target Market(s)

Customers, suppliers, business partners

Industry/Entity Type

Business

Contact Information for Business Card

Business cards should feature Company Name and Logo.

Font styles to use
Serif

Colors

Designer to choose colors to be used in the design.

Requirements
Must have
• Strong readability of Name, phone #, mobile number and email address.
• Job title, website url, Street Address, and other details can be secondary level readability.
Nice to have
• High impact, simplistic quality design.
• Ok to utilize the 'H in the box' separate from the company name

```html
<!DOCTYPE html>
<html lang="en">
<head>
<meta charset="utf-8">
<title>Lanternfield Drinks business cards</title>
<link rel="stylesheet" href="https://fonts.googleapis.com/css2?family=Lato:wght@400;700&family=Libre+Baskerville:wght@400;700&display=swap">
<style>
  :root {
    --backdrop: #b9b4b4;
    --card: #0b0b0b;
    --orange: #f15a29;
    --amber: #f7941d;
    --white: #ffffff;
  }
  html, body {
    margin: 0;
    padding: 0;
    width: 1200px;
    height: 900px;
    overflow: hidden;
    background: var(--backdrop);
  }
  .canvas {
    position: relative;
    width: 1200px;
    height: 900px;
  }
  .card {
    position: absolute;
    top: 200px;
    width: 310px;
    height: 502px;
    background: var(--card);
    overflow: hidden;
  }
  .card--front {
    left: 265px;
    border-radius: 62px 0 62px 0;
  }
  .card--back {
    left: 641px;
    border-radius: 0 62px 0 62px;
  }

  /* Front: brand block */
  .brand {
    position: absolute;
    left: 28px;
    top: 46px;
    display: flex;
    align-items: center;
    gap: 12px;
  }
  .brand__square {
    width: 22px;
    height: 22px;
    border: 4px solid var(--orange);
    box-sizing: border-box;
    flex: none;
  }
  .brand__name {
    font-family: "Libre Baskerville", serif;
    font-weight: 700;
    font-size: 18px;
    letter-spacing: 1px;
    line-height: 24px;
    color: var(--orange);
    text-transform: uppercase;
  }

  /* Front: contact block */
  .person {
    position: absolute;
    left: 25px;
    top: 286px;
    font-family: "Lato", sans-serif;
  }
  .person__name {
    margin: 0;
    font-size: 20px;
    font-weight: 700;
    color: var(--orange);
    line-height: 26px;
  }
  .person__title {
    margin: 0 0 9px;
    font-size: 14px;
    color: var(--amber);
    line-height: 18px;
  }
  .contact {
    list-style: none;
    margin: 0;
    padding: 0;
    color: var(--white);
    font-size: 14px;
  }
  .contact__item {
    display: flex;
    align-items: center;
    gap: 6px;
    line-height: 17px;
  }
  .contact__item--address {
    align-items: flex-start;
    margin-top: 8px;
    line-height: 18px;
  }
  .contact__icon {
    width: 12px;
    height: 12px;
    flex: none;
    fill: var(--orange);
  }
  .contact__item--address .contact__icon {
    margin-top: 3px;
  }

  /* Back: wordmark */
  .wordmark {
    position: absolute;
    left: 160px;
    top: 196px;
    width: 320px;
    height: 30px;
    line-height: 30px;
    transform: translate(-50%, -50%) rotate(-90deg);
    text-align: center;
    font-family: "Libre Baskerville", serif;
    font-weight: 700;
    font-size: 21px;
    letter-spacing: 0.5px;
    color: var(--orange);
    white-space: nowrap;
  }
  .back__rule {
    position: absolute;
    left: 194px;
    top: 36px;
    width: 2px;
    height: 320px;
    background: var(--amber);
  }
  .back__square {
    position: absolute;
    left: 108px;
    top: 372px;
    width: 93px;
    height: 93px;
    border: 4px solid var(--orange);
    box-sizing: border-box;
  }
</style>
</head>
<body>
<main class="canvas">

  <section class="card card--front" aria-label="Business card front">
    <div class="brand">
      <span class="brand__square"></span>
      <span class="brand__name">Lanternfield<br>Drinks</span>
    </div>

    <div class="person">
      <h1 class="person__name">LORUM SMITH</h1>
      <p class="person__title">Managing Director</p>
      <ul class="contact">
        <li class="contact__item">
          <svg class="contact__icon" viewBox="0 0 12 12"><path d="M1 4c0-1.5 2-2.5 5-2.5s5 1 5 2.5v1H8.5V4h-5v1H1z M2.5 6h7l1 4.5h-9z"/></svg>
          444 555 6688
        </li>
        <li class="contact__item">
          <svg class="contact__icon" viewBox="0 0 12 12"><path d="M3.5 0.5h5a1 1 0 0 1 1 1v9a1 1 0 0 1-1 1h-5a1 1 0 0 1-1-1v-9a1 1 0 0 1 1-1zM3.8 2v7h4.4V2z"/></svg>
          888 555 4433
        </li>
        <li class="contact__item">
          <svg class="contact__icon" viewBox="0 0 12 12"><path d="M1 3h10v6.5H1z" /><path d="M1 3l5 3.5L11 3" fill="none" stroke="#0b0b0b" stroke-width="1"/></svg>
          info@webname.com
        </li>
        <li class="contact__item">
          <svg class="contact__icon" viewBox="0 0 12 12"><circle cx="6" cy="6" r="5.5"/><path d="M3 4.5c1-.5 2 0 2.5 1S4.5 8 4 9M7.5 2.5c.5 1 1.5 1 2 2.5" fill="none" stroke="#0b0b0b" stroke-width="1"/></svg>
          www.webaddress.com
        </li>
        <li class="contact__item contact__item--address">
          <svg class="contact__icon" viewBox="0 0 12 12"><path d="M6 0.5a4 4 0 0 1 4 4c0 3-4 7-4 7s-4-4-4-7a4 4 0 0 1 4-4zm0 2.5a1.5 1.5 0 1 0 0 3 1.5 1.5 0 0 0 0-3z"/></svg>
          <span>421, Address line here,<br>Dummy Code, 45452<br>Country Name</span>
        </li>
      </ul>
    </div>
  </section>

  <section class="card card--back" aria-label="Business card back">
    <div class="back__rule"></div>
    <div class="wordmark">LANTERNFIELD DRINKS</div>
    <div class="back__square"></div>
  </section>

</main>
</body>
</html>
```